Modern Small Law Firm Website To Look Cutting Edge

I need a website design for a new, single-attorney law firm. The firm will be called "The Ashcombe Law Group." Our goal is to handle car accident and general personal injury lawsuits for individuals.

Our selling points are: (1) We charge less so you keep more; (2) We have experience and success trying and settling multi-million dollar cases; (3) We use modern technology to make the whole process simple, easy and hassle-free for clients.

Also because we are a one-man law firm, the clients will personally know the lawyer and have access to them. For that reason, I thought a good big tagline for the website would be "KNOW YOUR LAWYER"

I like the idea of splitting the website vertically down the middle, with the left side having a blue background, a picture of me, and big white lettering for the tagline, and the right side having a white background with blue lettering and headlines. I don't want navy blue or royal blue, but a more bright and eye-catching blue color. We can experiment with different shades.

I would be curious about how it could look with some minor orange accent coloring somewhere.

I need to feature prominently, probably in the top left corner, this phone number: 504-271-9038.

This will be used as much by mobile users as it would be by desktop/computer users.

The final design should communicate trust, convenience and cutting edge technology that leads to success.

Finally, I would be curious how we can have a sleek looking info submission box somewhere on the right side nearer the bottom that features different combinations of presenting these phrases: "QUICK QUESTION? QUICK ANSWER" The info submission button could say "Ask"

I am uploading two different pictures of me that can be used. The gray backgrounds are not necessary or good, if there is a way to cut them out that would be great. I can try and get that if needed.

Target Market(s)

Individuals who have been hurt by others, mostly in car accidents. They will be frustrated, inconvenienced and need to be soothed.

Industry/Entity Type

Legal

Number of Pages Required

1 page

Font styles to use
Sans Serif

Colors
0692cd
33a6d7
85cae6
faa54b
f78f20
3276b5

Requirements
Must have
• If you have started designing already, please note that the project description information is more important than the image that I uploaded originally. It has since been deleted.
• Also please now use the color photo that has been uploaded.
Nice to have
• I really want a clean and simple website design with not a lot of clutter. I'd like to avoid the typical law firm websites that you see that have tool bars across the top and basic borders/columns everywhere. It needs to grab your attention and look a little more cutting edge and different.
• Let's experiment with different eye-catching ways to present the three value propositions I noted.
• Also if the screen is split vertically with the left and right side being blue and white, maybe we can experiment with different ways that the two colors could fade into each other as opposed to just a line where one color starts and the other ends.
• And maybe the blue/white backgrounds could be textured somehow so that they don't appear flat. Perhaps we could try using differing shades of blue to give the appearance of pattern or 3D texture.
Should not have
• The basic picture/design I uploaded is just a suggestion, but there isn't really anything there.

```html
<!DOCTYPE html>
<html lang="en">
<head>
<meta charset="utf-8">
<title>The Ashcombe Law Group</title>
<link href="https://fonts.googleapis.com/css2?family=Open+Sans:wght@300;400;600;700&display=swap" rel="stylesheet">
<style>
:root{
  --blue:#0692cd;
  --blue-light:#4fc6fb;
  --blue-mid:#33a6d7;
  --blue-deep:#0a9be3;
  --orange:#f78f20;
  --orange-dark:#e57506;
  --ink:#333333;
  --muted:#555555;
  --panel:#f4f4f4;
  --footer:#2e2e2e;
  --line:#cfcfcf;
}
*{box-sizing:border-box;margin:0;padding:0}
html,body{width:798px;height:1200px;overflow:hidden;background:#fff}
body{position:relative;font-family:'Open Sans',Arial,sans-serif;color:var(--ink)}
.abs{position:absolute}

/* header */
.site-header{left:0;top:0;width:798px;height:83px;background:#fff}
.phone-icon{left:87px;top:27px;width:26px;height:26px}
.phone-number{left:126px;top:28px;font-size:16px;font-weight:400;color:#444;letter-spacing:.2px}
.brand{left:268px;top:26px;font-size:20px;font-weight:400;color:var(--blue);letter-spacing:1.5px}
.menu-icon{left:699px;top:32px;width:12px;height:10px}

/* hero */
.hero{left:0;top:83px;width:798px;height:291px;background:linear-gradient(100deg,#9a8f86 0%,#d6d1cb 22%,#3f9ed8 42%,#2d6aa8 55%,#47566f 75%,#6c7486 100%)}
.hero-title{left:246px;top:201px;width:307px;height:62px;background:rgba(40,40,40,.72);border:1px solid rgba(255,255,255,.15);color:#fff;font-size:25px;font-weight:400;text-align:center;line-height:60px;letter-spacing:.5px}
.dot{top:347px;width:6px;height:6px;border-radius:50%;background:#fff}

/* split */
.intro-left{left:0;top:374px;width:398px;height:496px;background:linear-gradient(180deg,var(--blue-light) 0%,#30b4f0 50%,var(--blue-deep) 100%)}
.initials{left:86px;top:400px;font-size:24px;font-weight:700;color:#fff;letter-spacing:1px}
.attorney-photo{left:90px;top:442px;width:207px;height:272px;background:linear-gradient(180deg,#3c90c4 0%,#2a2f3a 45%,#1d2028 100%)}
.tagline{left:0;top:740px;width:398px;text-align:center;color:#fff;font-size:33px;font-weight:700;line-height:38px;letter-spacing:.5px}

.point-title{left:426px;font-size:16px;font-weight:400;color:#222}
.point-text{left:425px;font-size:9px;line-height:13px;color:#333}

.quick-bar{left:425px;top:633px;width:285px;height:44px;background:linear-gradient(180deg,var(--orange) 0%,var(--orange-dark) 100%);color:#fff;font-size:12.5px;font-weight:700;line-height:44px;padding-left:13px;letter-spacing:.2px}
.field{border:1px solid var(--line);background:#fff;font-size:7.5px;color:#888;padding:11px 7px}
.ask{left:427px;top:803px;width:69px;height:28px;background:linear-gradient(180deg,var(--orange) 0%,var(--orange-dark) 100%);color:#fff;font-size:13px;font-weight:700;text-align:center;line-height:28px;border-radius:2px}

/* selling points */
.selling{left:0;top:870px;width:798px;height:212px;background:var(--panel)}
.selling-title{left:0;top:902px;width:840px;text-align:center;font-size:19px;font-weight:400;color:#333}
.sp-icon{top:948px;width:30px;height:28px}
.sp-text{top:997px;width:190px;text-align:center;font-size:10.3px;line-height:16px;color:#444}

/* footer */
.site-footer{left:0;top:1082px;width:798px;height:118px;background:var(--footer)}
.news-title{left:91px;top:1107px;font-size:16px;color:#fff;font-weight:400}
.news-input{left:88px;top:1143px;width:177px;height:29px;background:#fff;border-radius:2px;font-size:7px;color:#777;line-height:29px;padding-left:26px}
.mail-icon{left:99px;top:1153px;width:9px;height:7px}
.subscribe{left:273px;top:1143px;width:60px;height:30px;background:linear-gradient(180deg,#2f8ee0,#1b6fc2);color:#fff;font-size:7px;text-align:center;line-height:30px;border-radius:2px}
.copyright{left:480px;top:1112px;width:232px;text-align:right;font-size:7.5px;color:#fff}
.social{top:1141px;width:26px;height:26px;border:1px solid #777;border-radius:50%}
</style>
</head>
<body>

<header class="abs site-header">
  <svg class="abs phone-icon" viewBox="0 0 26 26" aria-hidden="true">
    <circle cx="13" cy="13" r="12.3" fill="none" stroke="#888" stroke-width="1"/>
    <path d="M9.6 8.2c.5-.4 1.1-.3 1.4.2l1 1.6c.3.5.2 1-.2 1.3l-.6.5c.5 1.3 1.5 2.4 2.8 3l.5-.6c.3-.4.9-.5 1.3-.2l1.6 1c.5.3.6.9.2 1.4l-.6.7c-.6.6-1.5.8-2.3.4-2.6-1.2-4.6-3.2-5.8-5.8-.4-.8-.2-1.7.4-2.3z" fill="#444"/>
  </svg>
  <div class="abs phone-number">504-271-9038</div>
  <div class="abs brand">ASHCOMBE LAW GROUP</div>
  <svg class="abs menu-icon" viewBox="0 0 12 10" aria-hidden="true">
    <rect width="12" height="2" fill="#222"/><rect y="4" width="12" height="2" fill="#222"/><rect y="8" width="12" height="2" fill="#222"/>
  </svg>
</header>

<section class="abs hero" role="img" aria-label="Photo of a man on the phone beside two cars after a collision"></section>
<div class="abs hero-title">KNOW YOUR LAWYER</div>
<span class="abs dot" style="left:379px"></span>
<span class="abs dot" style="left:395px;opacity:.6"></span>
<span class="abs dot" style="left:413px"></span>

<section class="abs intro-left"></section>
<div class="abs initials">ALG</div>
<div class="abs attorney-photo" role="img" aria-label="Portrait of the attorney in a dark suit and striped tie"></div>
<div class="abs tagline">CAR WRECK?<br>WE CAN HELP.</div>

<div class="abs point-title" style="top:412px">NEVER MORE THAN 24%</div>
<div class="abs point-text" style="top:440px">Our Lawyers will nerver Overcharge<br>You like others will.</div>
<div class="abs point-title" style="top:481px">WE MAKE IT EASY</div>
<div class="abs point-text" style="top:511px">These new brake pads are really<br>cool,youwon't believe it.</div>
<div class="abs point-title" style="top:550px">WE MAKE IT EASY</div>
<div class="abs point-text" style="top:582px">with experience in multi-million<br>dollar litigation, we're the best</div>

<div class="abs quick-bar">QUICK QUESTION? QUICK ANSWER</div>
<div class="abs field" style="left:426px;top:686px;width:90px;height:32px">Name</div>
<div class="abs field" style="left:525px;top:686px;width:89px;height:32px">Email</div>
<div class="abs field" style="left:621px;top:686px;width:89px;height:32px">Phone Number</div>
<div class="abs field" style="left:426px;top:724px;width:284px;height:71px;padding-top:10px">Your Message</div>
<div class="abs ask">Ask</div>

<section class="abs selling"></section>
<div class="abs selling-title">OUR SELLING POINTS ARE</div>

<svg class="abs sp-icon" style="left:160px" viewBox="0 0 30 28" aria-hidden="true">
  <path d="M6 8l2.5-5h13L24 8h2c1 0 2 1 2 2v8c0 1-1 1.5-2 1.5H4c-1 0-2-.5-2-1.5v-8c0-1 1-2 2-2z" fill="#444"/>
  <path d="M9 8l1.6-3.3h8.8L21 8z" fill="var(--panel)"/>
  <circle cx="8" cy="13" r="2" fill="var(--panel)"/><circle cx="22" cy="13" r="2" fill="var(--panel)"/>
  <rect x="4" y="19" width="5" height="5" rx="1" fill="#444"/><rect x="21" y="19" width="5" height="5" rx="1" fill="#444"/>
</svg>
<svg class="abs sp-icon" style="left:384px" viewBox="0 0 30 28" aria-hidden="true">
  <path d="M15 1L28 7v2H2V7z" fill="#444"/>
  <rect x="4" y="10" width="3" height="11" fill="#444"/><rect x="10" y="10" width="3" height="11" fill="#444"/>
  <rect x="17" y="10" width="3" height="11" fill="#444"/><rect x="23" y="10" width="3" height="11" fill="#444"/>
  <rect x="2" y="22" width="26" height="2" fill="#444"/><rect x="1" y="25" width="28" height="2.5" fill="#444"/>
</svg>
<svg class="abs sp-icon" style="left:607px" viewBox="0 0 30 28" aria-hidden="true">
  <g transform="rotate(45 13 10)">
    <rect x="5" y="4" width="16" height="10" rx="1" fill="#444"/>
    <rect x="11" y="14" width="4" height="15" fill="#444"/>
  </g>
</svg>

<div class="abs sp-text" style="left:80px">We charge less so you keep more;</div>
<div class="abs sp-text" style="left:304px">We have experience and success trying and settling multi-million dollar cases;</div>
<div class="abs sp-text" style="left:527px">We use modern technology to make the whole process simple, easy and hassle-free for clients.</div>

<footer class="abs site-footer"></footer>
<div class="abs news-title">NEWSLETTER</div>
<div class="abs news-input">ENTER YOUR MAIL ID</div>
<svg class="abs mail-icon" viewBox="0 0 9 7" aria-hidden="true">
  <rect x=".5" y=".5" width="8" height="6" fill="none" stroke="#777" stroke-width="1"/>
  <path d="M.5 .8L4.5 4l4-3.2" fill="none" stroke="#777" stroke-width="1"/>
</svg>
<div class="abs subscribe">SUBSCRIBE</div>
<div class="abs copyright">©2016 Ashcombe Law Group. All rights reserved.</div>
<span class="abs social" style="left:616px"></span>
<span class="abs social" style="left:649px"></span>
<span class="abs social" style="left:684px"></span>

</body>
</html>
```